Stationary/business card/envelope design for Larkvale Dentalcare

We are located in the foothills of the sierra nevada mountains. We are looking for a beautiful classy modern stationary. We need evelopes and business card design all to flow seamlessly. Envelope design.

Additional office address 4816 Meridian Wy., Suite B, Auburn, CA 95604 Phone: pending Fax: pending.

3 different Drs on each business card:
Helen R. Marsh, DDS
Orla P. Marsh, DDS
Rebecca S. Halvey, DDS

Target Market(s)

Dental patients

Industry/Entity Type

Dental

Contact Information for Business Card

Two sided. See example.

Font styles to use
Sans Serif

Requirements
Must have
• One sided business cards. Need envelope design.
Colors should match existing logo.

Helen R. Marsh, DDS
Orla P. Marsh, DDS
Rebecca S. Halvey, DDS

```html
<!DOCTYPE html>
<html lang="en">
<head>
<meta charset="utf-8">
<title>Larkvale Dentalcare – Business Card</title>
<link rel="stylesheet" href="https://fonts.googleapis.com/css2?family=Nunito:ital,wght@0,400;0,600;0,700;1,400&display=swap">
<style>
  :root {
    --bg: #2a2a2b;
    --card: #ffffff;
    --blue: #3aa6d2;
    --blue-soft: #bfe2f1;
    --green: #2f7d45;
    --grey: #505459;
    --radius: 26px;
  }
  * { box-sizing: border-box; margin: 0; padding: 0; }
  html, body {
    width: 1200px; height: 1200px; overflow: hidden;
    background: var(--bg);
    font-family: "Nunito", sans-serif;
  }
  .card-slot {
    position: absolute;
    left: 257px;
    width: 686px; height: 391px;
  }
  .card-slot--front { top: 166px; }
  .card-slot--back { top: 653px; }
  .card {
    position: absolute; left: 0; top: 0;
    width: 800px; height: 456px;
    transform: scale(0.8575);
    transform-origin: 0 0;
    background: var(--card);
    border-radius: var(--radius);
    overflow: hidden;
    box-shadow: 0 10px 24px rgba(0,0,0,.35);
  }

  /* Front */
  .brand-disc {
    position: absolute; left: -10px; top: -8px;
    width: 440px; height: 440px;
  }
  .brand-name {
    position: absolute; right: 40px; top: 44px;
    width: 340px; text-align: right;
    font-weight: 700; font-size: 44px; line-height: 1.05;
    color: var(--green);
  }
  .dentists {
    position: absolute; right: 47px; top: 170px;
    text-align: right;
  }
  .dentists li {
    list-style: none;
    font-weight: 700; font-size: 21.5px; line-height: 23px;
    color: var(--blue);
  }
  .tagline {
    position: absolute; right: 47px; top: 240px;
    font-size: 17px; color: var(--green); letter-spacing: .3px;
  }
  .contact {
    position: absolute; right: 44px; top: 281px;
    text-align: right;
  }
  .contact li {
    list-style: none;
    display: flex; justify-content: flex-end; align-items: center;
    font-size: 17px; line-height: 23px; color: var(--grey);
  }
  .contact .icon {
    width: 16px; height: 16px; margin-left: 10px; flex: none;
    fill: var(--blue);
  }
  .contact .icon--blank { visibility: hidden; }

  /* Back */
  .appt-title {
    position: absolute; left: 0; right: 0; top: 46px;
    text-align: center;
    font-size: 25px; font-weight: 600; letter-spacing: .4px;
    color: var(--blue);
  }
  .field-row {
    position: absolute; left: 54px; right: 56px;
    display: flex; align-items: flex-end;
    font-size: 17px; color: var(--blue);
  }
  .leader {
    flex: 1;
    border-bottom: 2px dotted var(--grey);
    margin: 0 4px 5px;
  }
  .leader:first-child { margin-left: 0; }
  .leader--time { flex: 0 0 188px; margin-right: 10px; }
  .row-patient { top: 112px; }
  .row-date { top: 167px; }
  .row-note { top: 277px; }
  .row-note2 { top: 322px; }
  .days {
    position: absolute; top: 227px; left: 0; width: 800px; height: 24px;
  }
  .day {
    position: absolute; top: 0;
    display: flex; align-items: center;
    font-size: 17px; color: var(--blue);
  }
  .day .box {
    width: 22px; height: 16px; margin-left: 7px;
    border: 2px solid var(--green);
  }
  .policy {
    position: absolute; left: 0; right: 0; top: 378px;
    text-align: center;
    font-style: italic; font-size: 16px; line-height: 21px;
    color: var(--grey);
  }
</style>
</head>
<body>

<div class="card-slot card-slot--front">
  <section class="card card--front">
    <svg class="brand-disc" viewBox="0 0 440 440" aria-hidden="true">
      <circle cx="220" cy="220" r="210" fill="var(--blue-soft)"/>
    </svg>

    <h1 class="brand-name">Larkvale Dentalcare</h1>

    <ul class="dentists">
      <li>Helen R. Marsh, DDS</li>
      <li>Orla P. Marsh, DDS</li>
      <li>Rebecca S. Halvey, DDS</li>
    </ul>
    <p class="tagline">Family &amp; Cosmetic Dentistry</p>

    <ul class="contact">
      <li>(530) 555-0142
        <svg class="icon" viewBox="0 0 16 16"><path d="M3.5 1.5l2.4-.3 1.3 3.1-1.6 1.3a8 8 0 0 0 4.8 4.8l1.3-1.6 3.1 1.3-.3 2.4c-.1.8-.8 1.3-1.6 1.3C7.4 13.8 2.2 8.6 2.2 3.1c0-.8.5-1.5 1.3-1.6z"/></svg>
      </li>
      <li>(530) 555-0187
        <svg class="icon" viewBox="0 0 16 16"><path d="M4 1h8v4H4zM2 6h12a1 1 0 0 1 1 1v5h-2v3H3v-3H1V7a1 1 0 0 1 1-1zm3 5v3h6v-3z"/></svg>
      </li>
      <li>larkvaledentalcare@mailbox.example
        <svg class="icon" viewBox="0 0 16 16"><path d="M1 3.5h14v9H1zM1.5 4l6.5 5 6.5-5" stroke="#fff" stroke-width="1.2"/></svg>
      </li>
      <li>www.larkvaledentalcare.example
        <svg class="icon" viewBox="0 0 16 16"><circle cx="8" cy="8" r="7"/><path d="M1 8h14M8 1c-3 3.5-3 10.5 0 14M8 1c3 3.5 3 10.5 0 14" stroke="#fff" stroke-width="1" fill="none"/></svg>
      </li>
      <li>4816 Meridian Wy.
        <svg class="icon" viewBox="0 0 16 16"><path d="M8 .5a5.5 5.5 0 0 0-5.5 5.5C2.5 10 8 15.5 8 15.5S13.5 10 13.5 6A5.5 5.5 0 0 0 8 .5zm0 3a2.5 2.5 0 1 1 0 5 2.5 2.5 0 0 1 0-5z"/></svg>
      </li>
      <li>Suite B, Auburn, CA 95604
        <svg class="icon icon--blank" viewBox="0 0 16 16"></svg>
      </li>
    </ul>
  </section>
</div>

<div class="card-slot card-slot--back">
  <section class="card card--back">
    <h2 class="appt-title">NEXT APPOINTMENT</h2>

    <div class="field-row row-patient">
      <span class="leader"></span><span>has an apppointment</span>
    </div>

    <div class="field-row row-date">
      <span>Date :</span><span class="leader"></span>
      <span>Time :</span><span class="leader leader--time"></span>
      <span>AM/PM</span>
    </div>

    <div class="days">
      <span class="day" style="left:100px">Sun<span class="box"></span></span>
      <span class="day" style="left:204px">Mon<span class="box"></span></span>
      <span class="day" style="left:309px">Tue<span class="box"></span></span>
      <span class="day" style="left:432px">Wed<span class="box"></span></span>
      <span class="day" style="left:538px">Thu<span class="box"></span></span>
      <span class="day" style="left:648px">Fri<span class="box"></span></span>
    </div>

    <div class="field-row row-note">
      <span>Note :</span><span class="leader"></span>
    </div>
    <div class="field-row row-note2">
      <span class="leader"></span>
    </div>

    <p class="policy">Please give me 24 hours notice if you are unable to keep your appointment<br>or a cancellation fee may be charged.</p>
  </section>
</div>

</body>
</html>
```